Two (Similar) Posters - Both 11" x 17"

We are looking for two posters - both 11" x 17" (vertical orientation) - to promote two consecutive, cardiology-related events:

Poster #1) The Inaugural New York ROC Brainbuzz Competition, Cocktail Reception and Whiskey Tasting (http://hb-pvl.org/brainbuzz-and-reception)

and

Poster #2) The 89th Annual Scientific Session and 27th Annual Meeting (http://hb-pvl.org/2017annualmtg)

#1 is a cocktail party with a whiskey tasting that will also feature a gameshow-like event with the med students, and #2 is an educational conference for doctors

Target Market(s)

Healthcare providers (Please do not include stock images of medical professionals; in fact, please use caution with any stock imagery, as it most likely will not be appropriate.)

Industry/Entity Type

Education

Colors

Designer to choose colors to be used in the design.

Requirements
Must have
• Each poster design should include:
• - the 4 logos of the participating organizations (I can upload various other versions if needed) along with the "wording" that goes alongside each one (see "STD_small" image as an example)
• - name of event
• - date, time and location
• - where to register
• - where to get more information
• - some artistic flavor or detailing
• Final (raw) files in an .ai, .psd, .eps or .idml format are required upon project completion.
Nice to have
• It's not crucial that these two posters "match," but it would be nice if they at least coordinated with each other. Would be nice if the designer could stay close to our color scheme (can be found here - http://hb-pvl.org/), but this isn't crucial. Posters should be upscale, neat and professional.
Should not have
• Should not be too difficult to read. These are posters that will likely be hanging on a bulletin board in hospital staff break rooms. Should not be too cartoon-like or silly. The two should not look EXACTLY the same in case people think that they are the same poster.

```html
<!DOCTYPE html>
<html lang="en">
<head>
<meta charset="utf-8">
<title>Event Posters</title>
<link href="https://fonts.googleapis.com/css2?family=Cinzel:wght@400;600&family=Tinos:ital,wght@0,400;0,700;1,400&display=swap" rel="stylesheet">
<style>
:root{
  --navy:#1f3a63;
  --gold:#c9a45c;
  --paper:#ffffff;
  --ink:#141414;
  --stage:#d6d6d6;
  --band:#e9e9e9;
  --box-ink:#2a2a2a;
}
*{box-sizing:border-box;margin:0;padding:0}
html,body{width:1200px;height:831px;overflow:hidden}
body{background:var(--stage);position:relative;font-family:"Tinos",serif;color:var(--ink)}
.poster{position:absolute}
.poster--reception{left:50px;top:60px;width:450px;height:688px}
.poster--session{left:670px;top:53px;width:456px;height:695px}
.photo-strip{position:absolute;left:0;right:0;height:54px}
.photo-strip--top{top:0}
.photo-strip--bottom{bottom:0;background:linear-gradient(90deg,#3b2a1c 0%,#7a5530 14%,#c98a45 24%,#4a3426 34%,#2b2a55 48%,#5d4fb0 56%,#2a2440 66%,#6b4a2a 78%,#b8843f 88%,#4a3120 100%)}
.poster--reception .photo-strip--top{background:linear-gradient(90deg,#3a2c6a 0%,#7d5bb8 14%,#2a1e3a 32%,#b84a7a 46%,#3a2a30 60%,#6a5a4a 78%,#2a2430 100%)}
.poster--session .photo-strip--top{background:linear-gradient(90deg,#6a5230 0%,#a8844a 18%,#3a2e22 34%,#2a2a6a 46%,#6a5ad0 56%,#2a2440 66%,#8a5a2a 78%,#c9904a 88%,#4a3220 100%)}
.panel{position:absolute;left:0;right:0;top:54px;bottom:54px;background:var(--navy)}
.frame{position:absolute;background:var(--gold)}
.poster--reception .frame{left:18px;top:76px;width:414px;height:534px}
.poster--session .frame{left:18px;top:75px;width:420px;height:543px}
.sheet{position:absolute;inset:6px;background:var(--paper)}
.sheet::after{content:"";position:absolute;inset:4px;border:1.5px solid var(--gold)}
.line{position:absolute;left:0;right:0;text-align:center;white-space:nowrap}
.ornament{position:absolute;left:50%;width:300px;height:6px;margin-left:-150px;border-radius:3px;background:linear-gradient(90deg,transparent,var(--navy) 8%,var(--navy) 92%,transparent)}
.title{font-family:"Cinzel",serif;color:var(--navy);font-weight:400;letter-spacing:.5px}
.subtitle{font-family:"Cinzel",serif;font-size:10px;letter-spacing:.6px}
.date{font-weight:700;color:var(--navy);font-size:22px;line-height:24px}
.when{font-weight:700;font-size:11.5px;line-height:14px}
.venue{font-weight:700;color:var(--navy);font-size:22px;line-height:24px}
.address{font-weight:700;font-size:11.5px;line-height:14px}
.register{font-family:"Cinzel",serif;font-size:14px;line-height:16px;letter-spacing:.6px}
.url{font-weight:700;color:var(--navy);font-size:13px;line-height:15px}
.info{font-weight:700;font-size:10px;line-height:12px}
.contacts{display:flex;justify-content:center;align-items:center;gap:10px;font-weight:700;font-size:10px;line-height:12px}
.contact{display:flex;align-items:center;gap:6px}
.contact svg{width:9px;height:9px}
.price{position:absolute;border-radius:50%;display:flex;flex-direction:column;align-items:center;justify-content:center;text-align:center;background:var(--paper)}
.price--free{left:41px;top:310px;width:104px;height:104px;border:3.5px solid var(--gold)}
.price--paid{left:292px;top:304px;width:108px;height:108px;border:3.5px solid var(--navy)}
.price-amount{font-family:"Cinzel",serif;font-size:21px;line-height:22px}
.price--free .price-amount{color:var(--navy)}
.price--paid .price-amount{color:var(--gold)}
.price-note{font-weight:700;font-size:6.6px;line-height:9px;margin-top:2px}
.price--free .price-note{color:var(--navy)}
.price--paid .price-note{color:var(--gold);font-weight:400}
.about{position:absolute;left:37px;top:411px;width:382px;height:87px;background:var(--gold);padding:3px}
.about-inner{width:100%;height:100%;border:1.5px solid var(--navy);padding:7px 11px;font-size:7.6px;line-height:10.3px;color:var(--box-ink);text-align:justify}
.partners{position:absolute;display:flex;justify-content:space-between;align-items:center}
.poster--reception .partners{left:28px;right:28px;top:560px;height:28px}
.poster--session .partners{left:28px;right:28px;top:555px;height:48px}
.partners-band{position:absolute;left:28px;right:28px;top:553px;height:52px;background:var(--band)}
.partner{display:flex;align-items:center;gap:4px}
.partner-mark{display:flex;align-items:center;gap:2px}
.partner-mark i{display:block;width:20px;height:20px;border-radius:50%;border:1.5px solid var(--navy)}
.partner-name{font-weight:700;font-size:6px;color:var(--navy)}
.partner-caption{font-size:5px;line-height:6px;color:var(--navy);max-width:64px}
.partner-caption em{display:block;font-style:italic}
</style>
</head>
<body>

<section class="poster poster--reception">
  <div class="photo-strip photo-strip--top" role="img" aria-label="Photo strip of a stage and audience at a game show evening"></div>
  <div class="panel"></div>
  <div class="frame"><div class="sheet"></div></div>

  <div class="ornament" style="top:110px" role="img" aria-label="Decorative scroll flourish"></div>
  <h1 class="line title" style="top:140px;font-size:21px;line-height:24px">The Inaugural New York</h1>
  <h2 class="line title" style="top:165px;font-size:16px;line-height:18px">ROC Brainbuzz Competition</h2>
  <p class="line subtitle" style="top:189px">Cocktail Reception &amp; Whiskey Tasting</p>
  <p class="line date" style="top:207px">December 6th, 2017</p>
  <p class="line when" style="top:233px">Wednesday, from 6:30 p.m. to 10:30 p.m.</p>
  <p class="line venue" style="top:256px">Oak &amp; Ember</p>
  <p class="line address" style="top:282px">14 W 41st St, New York, NY 10018</p>

  <div class="price price--free">
    <span class="price-amount">FREE</span>
    <span class="price-note">for HBPVL/PVL Members</span>
  </div>
  <div class="price price--paid">
    <span class="price-amount">$30</span>
    <span class="price-note">for nonmembers and guests</span>
  </div>

  <p class="line register" style="top:409px">Register Online</p>
  <p class="line url" style="top:428px">hb-pvl.org/2017annualmtg</p>
  <p class="line info" style="top:452px">For more information or to inquire about becoming an exhibitor</p>
  <div class="line contacts" style="top:468px">
    <span class="contact"><svg viewBox="0 0 10 10"><circle cx="5" cy="5" r="5" fill="#1f3a63"/><path d="M3.2 2.6c.4-.3.7 0 .9.5l.2.6c.1.3-.1.5-.3.7.3.7.8 1.2 1.5 1.5.2-.2.4-.4.7-.3l.6.2c.5.2.8.5.5.9-.5.7-1.3.8-2.4.1C3.7 6.2 3 5.3 2.8 4.1c-.1-.6.1-1.2.4-1.5z" fill="#fff"/></svg>(212) 555-0147</span>
    <span>or</span>
    <span class="contact"><svg viewBox="0 0 10 10"><circle cx="5" cy="5" r="5" fill="#1f3a63"/><rect x="2.6" y="3.3" width="4.8" height="3.4" fill="none" stroke="#fff" stroke-width=".7"/><path d="M2.6 3.3L5 5.2l2.4-1.9" fill="none" stroke="#fff" stroke-width=".7"/></svg>ask@hb-pvl.org</span>
  </div>
  <div class="ornament" style="top:513px" role="img" aria-label="Decorative scroll flourish"></div>

  <div class="partners">
    <div class="partner"><span class="partner-mark"><i></i><span class="partner-name">HVCS</span></span><span class="partner-caption"><em>Presented by</em>The Hudson Valley Cardiological Society, Inc</span></div>
    <div class="partner"><span class="partner-mark"><i></i><span class="partner-name">HBSC</span></span><span class="partner-caption"><em>of the</em>The Hudson Bay State Chapter Pavilion College Of Cardiology</span></div>
    <div class="partner"><span class="partner-mark"><i></i><span class="partner-name">HCC</span></span><span class="partner-caption"><em>In Association With</em>Hudson Cardiac Center</span></div>
    <div class="partner"><span class="partner-mark"><i></i><span class="partner-name">PVL</span></span></div>
  </div>

  <div class="photo-strip photo-strip--bottom" role="img" aria-label="Photo strip of the lounge, bar and ballroom interiors"></div>
</section>

<section class="poster poster--session">
  <div class="photo-strip photo-strip--top" role="img" aria-label="Photo strip of the ballroom, stage and lounge interiors"></div>
  <div class="panel"></div>
  <div class="frame"><div class="sheet"></div></div>

  <div class="ornament" style="top:110px" role="img" aria-label="Decorative scroll flourish"></div>
  <h1 class="line title" style="top:147px;font-size:17.5px;line-height:20px">The 89th Annual Scientific Session &amp;</h1>
  <h2 class="line title" style="top:169px;font-size:14px;line-height:16px">27th Annual Meeting</h2>
  <p class="line date" style="top:194px">December 7th, 2017</p>
  <p class="line when" style="top:220px">Thursday, from 7:30 a.m. to 3 p.m.</p>
  <p class="line venue" style="top:246px;font-size:20px">The Marlowe Grand Ballroom</p>
  <p class="line address" style="top:271px">22 E. 31st St., New York, NY</p>

  <p class="line register" style="top:316px">Register Online</p>
  <p class="line url" style="top:336px">hb-pvl.org/2017annualmtg</p>
  <p class="line info" style="top:364px">For more information or to inquire about becoming an exhibitor</p>
  <div class="line contacts" style="top:380px">
    <span class="contact"><svg viewBox="0 0 10 10"><circle cx="5" cy="5" r="5" fill="#1f3a63"/><path d="M3.2 2.6c.4-.3.7 0 .9.5l.2.6c.1.3-.1.5-.3.7.3.7.8 1.2 1.5 1.5.2-.2.4-.4.7-.3l.6.2c.5.2.8.5.5.9-.5.7-1.3.8-2.4.1C3.7 6.2 3 5.3 2.8 4.1c-.1-.6.1-1.2.4-1.5z" fill="#fff"/></svg>(212) 555-0147</span>
    <span>or</span>
    <span class="contact"><svg viewBox="0 0 10 10"><circle cx="5" cy="5" r="5" fill="#1f3a63"/><rect x="2.6" y="3.3" width="4.8" height="3.4" fill="none" stroke="#fff" stroke-width=".7"/><path d="M2.6 3.3L5 5.2l2.4-1.9" fill="none" stroke="#fff" stroke-width=".7"/></svg>ask@hb-pvl.org</span>
  </div>

  <div class="about"><p class="about-inner">The Annual Scientific Session brings together cardiologists, cardia-thoracic surgeons, internists, family practitioners, gerontologists, oncologists, cardiac nurse practitioners, physician assistants, cardiology fellows in training (ROCs) and all members of the cardiac care team, and, this year, will feature the winners of the Annual Young Investigators' Competition for case studies and abstracts (posters), which is now open!</p></div>

  <div class="ornament" style="top:532px" role="img" aria-label="Decorative scroll flourish"></div>

  <div class="partners-band"></div>
  <div class="partners">
    <div class="partner"><span class="partner-mark"><i></i><span class="partner-name">HVCS</span></span><span class="partner-caption"><em>Presented by</em>The Hudson Valley Cardiological Society, Inc</span></div>
    <div class="partner"><span class="partner-mark"><i></i><span class="partner-name">HBSC</span></span><span class="partner-caption"><em>of the</em>The Hudson Bay State Chapter Pavilion College Of Cardiology</span></div>
    <div class="partner"><span class="partner-mark"><i></i><span class="partner-name">HCC</span></span><span class="partner-caption"><em>In Association With</em>Hudson Cardiac Center</span></div>
    <div class="partner"><span class="partner-mark"><i></i><span class="partner-name">PVL</span></span></div>
  </div>

  <div class="photo-strip photo-strip--bottom" role="img" aria-label="Photo strip of the lounge, bar and ballroom interiors"></div>
</section>

</body>
</html>
```